Vexo Systems Web Site Design

Need a basic site to show clients a little about what we do. We are a custom audio video company in the high-end residential market. Need a few basic but professional pages to show past projects and products we sell. No e-commerce. Should include my new logo from ArtHivePro.

Industry/Entity Type

Residential

Number of Pages Required

2 page

Font styles to use
Serif
Sans Serif

Colors
f78f20

Requirements
Must have
• Company Logo, Send feedback page
Nice to have
• I have no ideas about design, but I do know what I like and dislike when I see it.

```html
<!DOCTYPE html>
<html lang="en">
<head>
<meta charset="utf-8">
<title>Vexo Systems</title>
<link href="https://fonts.googleapis.com/css2?family=Oswald:wght@400;500&family=Open+Sans:wght@400;600;700&display=swap" rel="stylesheet">
<style>
:root{
  --orange:#f78f20;
  --ink:#2b2b2b;
  --text:#555;
  --muted:#8a8a8a;
  --line:#e2e2e2;
  --band:#f3f4f4;
  --footer:#1e1e1e;
  --footer-text:#9a9a9a;
  --white:#fff;
}
*{margin:0;padding:0;box-sizing:border-box}
html,body{width:797px;height:1200px;overflow:hidden;background:var(--white)}
body{position:relative;font-family:"Open Sans",Arial,sans-serif;color:var(--text)}
.abs{position:absolute}

/* header */
.site-header{position:absolute;left:0;top:0;width:797px;height:66px;background:var(--white)}
.brand{position:absolute;left:48px;top:14px;display:flex;align-items:center;gap:8px}
.brand-mark{width:34px;height:34px;background:var(--orange);border-radius:3px}
.brand-name{font-family:"Oswald",sans-serif;font-size:15px;font-weight:500;line-height:15px;color:var(--ink);letter-spacing:.5px}
.social{position:absolute;left:506px;top:12px;display:flex;gap:6px}
.social span{width:16px;height:16px;border-radius:50%;background:#c9c9c9}
.search{position:absolute;left:617px;top:10px;width:130px;height:20px;border:1px solid #ddd;border-radius:10px;font-size:7.5px;color:#999;padding:5px 9px}
.search svg{position:absolute;right:7px;top:5px}
.main-nav{position:absolute;right:50px;top:46px;display:flex;gap:21px;font-size:8.5px;color:var(--ink);letter-spacing:.2px}

/* hero */
.hero{position:absolute;left:0;top:66px;width:797px;height:344px;
  background:radial-gradient(ellipse at 50% 35%,#3b4fa0 0%,#1f2347 30%,#2a1a14 65%,#1a100b 100%)}
.hero-title{position:absolute;left:0;top:170px;width:797px;text-align:center;font-family:"Oswald",sans-serif;font-size:19px;line-height:23px;color:var(--white);letter-spacing:.2px}
.dots{position:absolute;left:384px;top:315px;display:flex;gap:3px}
.dots span{width:7px;height:7px;border-radius:50%;background:#888}
.dots span:first-child{background:var(--white)}

/* welcome */
.welcome{position:absolute;left:0;top:410px;width:797px;height:178px;background:var(--band);text-align:center}
.welcome h1{position:absolute;left:0;top:17px;width:797px;font-family:"Oswald",sans-serif;font-weight:400;font-size:20px;color:var(--ink)}
.accent{color:var(--orange)}
.welcome p{position:absolute;left:104px;top:52px;width:590px;font-size:8.3px;line-height:16px;color:var(--text)}
.btn{position:absolute;left:365px;top:129px;width:67px;height:19px;border-radius:10px;background:#bdbdbd;color:var(--white);font-size:7px;line-height:19px}

/* listings */
.section-title{position:absolute;font-family:"Oswald",sans-serif;font-weight:400;font-size:18px;color:var(--ink)}
.arrows{position:absolute;font-size:13px;color:var(--ink);letter-spacing:2px}
.arrows .dim{color:#aaa}
.divider{position:absolute;left:398px;top:608px;width:1px;height:352px;background:var(--line)}
.card{position:absolute;width:350px;height:92px}
.card .thumb{position:absolute;left:0;top:0;width:133px;height:92px}
.card h3{position:absolute;left:150px;top:-2px;font-size:10.5px;font-weight:600;color:var(--ink)}
.card p{position:absolute;left:150px;top:16px;width:190px;font-size:8.2px;line-height:13.5px;color:var(--text)}
.card a{position:absolute;left:150px;top:82px;font-size:8px;color:var(--orange);text-decoration:none}

/* footer */
.site-footer{position:absolute;left:0;top:1000px;width:797px;height:200px;background:var(--footer)}
.footer-brand{position:absolute;left:48px;top:55px;display:flex;align-items:center;gap:8px;opacity:.35}
.footer-brand .brand-mark{background:#9a9a9a}
.footer-brand .brand-name{color:#bbb}
.legal{position:absolute;left:48px;top:126px;font-size:7.5px;line-height:12px;color:#6a6a6a;width:160px}
.col{position:absolute;top:30px;width:162px}
.col h4{font-size:9px;font-weight:700;color:var(--white);margin-bottom:12px}
.post{font-size:7px;color:#777;border-bottom:1px solid #333;padding-bottom:12px;margin-bottom:10px}
.post:last-child{border:none}
.post b{display:block;font-weight:400;font-size:7.8px;line-height:13px;color:#cfcfcf;margin-top:5px}
.contact{display:flex;gap:12px;margin-bottom:14px;font-size:7.8px;line-height:12px;color:#cfcfcf}
.contact .ico{flex:0 0 22px;height:22px;border-radius:50%;background:#444;display:flex;align-items:center;justify-content:center}
</style>
</head>
<body>

<header class="site-header">
  <div class="brand"><div class="brand-mark"></div><div class="brand-name">VEXO<br>SYSTEMS</div></div>
  <div class="social"><span></span><span></span><span></span><span></span><span></span></div>
  <div class="search">Enter Your Keyword
    <svg width="9" height="9" viewBox="0 0 10 10"><circle cx="4" cy="4" r="3" fill="none" stroke="#aaa" stroke-width="1.2"/><line x1="6.3" y1="6.3" x2="9" y2="9" stroke="#aaa" stroke-width="1.2"/></svg>
  </div>
  <nav class="main-nav"><span>WE ARE VEXO</span><span>PORTFOLIO</span><span>SYSTEMS</span><span>SERVICES</span><span>WHY VEXO?</span><span>RESOURCES</span><span>BLOG</span><span>LOCATIONS</span><span>CONTACT</span></nav>
</header>

<section class="hero" role="img" aria-label="Photo of a dark home theater room with a lit projection screen and rows of leather recliners">
  <div class="hero-title">A HANDY LOREM IPSUM GENERATOR THAT<br>HELPS TO CREATE DUMMY TEXT</div>
  <div class="dots"><span></span><span></span><span></span></div>
</section>

<section class="welcome">
  <h1>WELCOME TO <span class="accent">VEXO SYSTEMS</span></h1>
  <p>In publishing and graphic design, lorem ipsum is a filler text commonly used to demonstrate the graphic elements of a document or visual presentation. Replacing meaningful content with placeholder text allows viewers to focus on graphic aspects such as font, typography, and page layout without being distracted by the content. It also reduces the need for the designer to come up with meaningful text, as they can instead use quickly-generated lorem ipsum.</p>
  <div class="btn">READ MORE</div>
</section>

<h2 class="section-title" style="left:48px;top:605px">PAST <span class="accent">PROJECTS</span></h2>
<div class="arrows" style="left:360px;top:609px"><span class="dim">‹</span>›</div>
<div class="divider"></div>
<h2 class="section-title" style="left:419px;top:605px">OUR <span class="accent">PRODUCTS</span></h2>
<div class="arrows" style="left:732px;top:609px"><span class="dim">‹</span>›</div>

<div class="card" style="left:48px;top:652px">
  <div class="thumb" role="img" aria-label="Living room with wall-mounted TV and media console" style="background:linear-gradient(135deg,#e8e3da,#b9a68a 60%,#5a4634)"></div>
  <h3>Lorem ipsum text is typically</h3>
  <p>Replacing meaningful content with placeholder text allows viewers to focus on graphic aspects such as font, typography, and without being distracted by the content.</p>
  <a>[Read More]</a>
</div>
<div class="card" style="left:48px;top:762px">
  <div class="thumb" role="img" aria-label="Home theater with projection screen and seating" style="background:linear-gradient(160deg,#2a2c4a,#3f3a5a 40%,#4a3424 80%)"></div>
  <h3>Lorem ipsum text is typically</h3>
  <p>Replacing meaningful content with placeholder text allows viewers to focus on graphic aspects such as font, typography, and without being distracted by the content.</p>
  <a>[Read More]</a>
</div>
<div class="card" style="left:48px;top:872px">
  <div class="thumb" role="img" aria-label="Warm-lit family room with TV and leather seating" style="background:linear-gradient(135deg,#6b3a1c,#c98a45 50%,#2b1a10)"></div>
  <h3>Lorem ipsum text is typically</h3>
  <p>Replacing meaningful content with placeholder text allows viewers to focus on graphic aspects such as font, typography, and without being distracted by the content.</p>
  <a>[Read More]</a>
</div>

<div class="card" style="left:419px;top:652px">
  <div class="thumb" role="img" aria-label="Silver stereo amplifier with speakers" style="background:linear-gradient(135deg,#f2f4f6,#c8ced4 60%,#9aa2aa)"></div>
  <h3>Lorem ipsum text is typically</h3>
  <p>Replacing meaningful content with placeholder text allows viewers to focus on graphic aspects such as font, typography, and without being distracted by the content.</p>
  <a>[Read More]</a>
</div>
<div class="card" style="left:419px;top:762px">
  <div class="thumb" role="img" aria-label="Wall-mounted touch control panel" style="background:radial-gradient(ellipse at 55% 45%,#2f8fe0 0%,#1a4f8a 35%,#3a2a1a 75%)"></div>
  <h3>Lorem ipsum text is typically</h3>
  <p>Replacing meaningful content with placeholder text allows viewers to focus on graphic aspects such as font, typography, and without being distracted by the content.</p>
  <a>[Read More]</a>
</div>
<div class="card" style="left:419px;top:872px">
  <div class="thumb" role="img" aria-label="Close-up of a projector lens" style="background:radial-gradient(circle at 50% 45%,#4a4a4a,#1a1a1a 45%,#d8d8d8 90%)"></div>
  <h3>Lorem ipsum text is typically</h3>
  <p>Replacing meaningful content with placeholder text allows viewers to focus on graphic aspects such as font, typography, and without being distracted by the content.</p>
  <a>[Read More]</a>
</div>

<footer class="site-footer">
  <div class="footer-brand"><div class="brand-mark"></div><div class="brand-name">VEXO<br>SYSTEMS</div></div>
  <div class="legal">© 2015 Vexo Systems. All Rights Reserved<br>Terms and Conditions | Privacy Policy |<br>Terms of Use</div>

  <div class="col" style="left:228px">
    <h4>RECENT BLOG</h4>
    <div class="post">10 MAR 2015 | 10 Comments<b>Mirum est notare quam littera gothi ca, quam nunc</b></div>
    <div class="post">10 MAR 2015 | 10 Comments<b>Mirum est notare quam littera gothi ca, quam nunc</b></div>
  </div>
  <div class="col" style="left:407px">
    <h4>RECENT NEWS</h4>
    <div class="post">10 MAR 2015<b>Mirum est notare quam littera gothi ca, quam nunc</b></div>
    <div class="post">10 MAR 2015<b>Mirum est notare quam littera gothi ca, quam nunc</b></div>
  </div>
  <div class="col" style="left:586px">
    <h4>GET IN TOUCH</h4>
    <div class="contact"><span class="ico"><svg width="9" height="11" viewBox="0 0 10 12"><path d="M5 0a4 4 0 0 0-4 4c0 3 4 8 4 8s4-5 4-8a4 4 0 0 0-4-4z" fill="#fff"/><circle cx="5" cy="4" r="1.5" fill="#444"/></svg></span><span>228, Lorem ipsum dolor amet<br>sit aremt sor- 859584</span></div>
    <div class="contact"><span class="ico"><svg width="10" height="10" viewBox="0 0 10 10"><path d="M2 0.5l1.8 2-1 1.2a6 6 0 0 0 3.5 3.5l1.2-1 2 1.8-1.2 1.6C4.5 9.3.7 5.5.4 1.7z" fill="#fff"/></svg></span><span>Phone :<br>(008) 88 888 8888</span></div>
    <div class="contact"><span class="ico"><svg width="10" height="8" viewBox="0 0 10 8"><rect x="0.5" y="0.5" width="9" height="7" fill="none" stroke="#fff"/><path d="M0.5 0.5l4.5 4 4.5-4" fill="none" stroke="#fff"/></svg></span><span>Email :<br>info@vexosystems.com</span></div>
  </div>
</footer>

</body>
</html>
```